Hypnotherapy- past life regression-life between lives therapist needs a website

I need a website that is enticing and spiritual in its feeling. It needs to have a lot of beautiful nature pictures included. The theme is "Willowmere Hollow- what could you uncover....Tides Lanterns Compass"
Because all of us have the answers to living our best life, they are in our subconcious. But not everyone is capable of accessing them. Hypnosis accesses the subconcious and helps to create new neural pathways in the brain which can create new behaviors and responses to situations.
Hypnosis can help with anxiety, pain relief, weight loss, smoking/vaping cessation, self confidence......anything about yourself that you want to change.
Exploration of past lives and life between lives can reveal things related to ones current life. For example, perhaps your fear of deep water is a result of drowning in a past life. Once this has been discovered, it can lead to changes in ones current life.
Almost any personal behavior one wants to change, can be helped through hypnotherapy.
I need a page for testimonials, a place for scheduling (I will have a link to my scheduling app) some information about hypnotherapy.
I am uploading my logo files. My business card will be using the black and gold style, but my website does not have to reflect that. It can be based on the caramel and deep green like full color logo. Earthy, calm colors.
I also like the mock up of my logo on the beach and there was one on a starry night sky that I also liked.
Target Market(s)
men and women ages 25-50
Industry/Entity Type
natural health and wellness, spirituality
Number of Pages Required
4 page
Requirements
Must have
- a page for testimonials, perhaps with a beautiful nature picture with each one, I will have approximately 6. A link to schedule a complimentary intro session, preferably on the first page
Should not have
- no swinging watches or other sterotyped hypnosis symbols

```html
<!DOCTYPE html>
<html lang="en">
<head>
<meta charset="utf-8">
<title>Willowmere Hollow — Hypnotherapy</title>
<link href="https://fonts.googleapis.com/css2?family=Cinzel:wght@400;500;600&family=Montserrat:wght@500;600;700&family=Roboto:wght@400;500&family=Open+Sans:ital@1&display=swap" rel="stylesheet">
<style>
:root{
  --caramel:#E0862A;
  --olive:#5B5A2F;
  --olive-dark:#4F4E28;
  --peach:#F3DFCB;
  --mist:#F7F7F7;
  --ink:#222;
  --body:#6b6b6b;
  --white:#fff;
}
*{box-sizing:border-box;margin:0;padding:0}
html,body{width:1200px;height:3854px;overflow:hidden;background:var(--white)}
body{position:relative;font-family:'Roboto',sans-serif;color:var(--ink)}
.abs{position:absolute}
.hero-photo{left:0;top:0;width:1200px;height:700px;
  background:radial-gradient(ellipse 260px 320px at 640px 40px,rgba(220,200,140,.55),transparent 70%),
  linear-gradient(180deg,#1c2417 0%,#2d3826 35%,#37432c 60%,#2a3322 100%)}
.waves{left:0;top:0;width:1200px;height:3854px}
.brand{font-family:'Cinzel',serif;font-weight:600;color:var(--white);text-align:center;line-height:1.1}
.nav{left:362px;top:66px;display:flex;gap:0}
.nav a{position:absolute;font-family:'Montserrat',sans-serif;font-weight:500;font-size:16px;color:var(--white);text-decoration:none;white-space:nowrap}
.btn{display:flex;align-items:center;justify-content:center;background:var(--caramel);color:var(--white);font-family:'Montserrat',sans-serif;font-weight:700;border-radius:30px;text-decoration:none}
.hero-title{left:300px;top:188px;width:600px;text-align:center;font-family:'Cinzel',serif;font-size:34px;line-height:42px;color:var(--white);font-weight:500}
.dot{width:7px;height:7px;border-radius:50%;background:var(--white)}
.section-title{font-family:'Cinzel',serif;color:var(--olive);font-size:45px;display:flex;align-items:center;gap:12px;white-space:nowrap}
.section-title .rule{height:3px;background:var(--olive)}
.light .rule{background:var(--white)}
.about-text{left:600px;top:690px;width:456px;font-size:14.5px;line-height:25.6px;color:var(--body);text-align:justify}
.ph{display:flex;align-items:center;justify-content:center}
.svc-label{font-size:18px;font-weight:500;color:var(--ink)}
.svc-desc{font-size:12.5px;line-height:20px;color:var(--body)}
.icon-ring{width:72px;height:72px;border-radius:50%;display:flex;align-items:center;justify-content:center}
.quote-card{top:2115px;width:301px;height:146px;border:2px solid #d8d8d8;background:var(--white);padding:22px 18px}
.quote-card p{font-family:'Open Sans',sans-serif;font-style:italic;font-size:10px;line-height:19px;color:#777}
.quote-card .who{margin-top:8px;font-size:12.5px;color:var(--ink)}
.avatar{width:82px;height:90px;clip-path:polygon(50% 0,100% 25%,100% 75%,50% 100%,0 75%,0 25%);background:linear-gradient(160deg,#c9b29a,#6e5a48)}
.stars{font-size:15px;letter-spacing:4px}
.arrow{width:34px;height:34px;border-radius:50%;border:2px solid #888;display:flex;align-items:center;justify-content:center}
.svc-card{top:2718px;width:281px;height:464px;background:var(--white);border:4px solid var(--white);box-shadow:0 0 0 1px rgba(255,255,255,.6)}
.svc-card .photo{height:206px}
.svc-card h3{margin-top:42px;text-align:center;font-weight:500;font-size:19.5px;color:#333}
.svc-card p{margin:8px auto 0;width:236px;text-align:center;font-size:15px;line-height:21px;color:#777}
.svc-card .btn{margin:28px auto 0;width:138px;height:33px;font-size:12px}
.form-field{border:1px solid #ccc;font-size:10.5px;color:#666;padding:8px 10px;background:var(--white)}
.form-h{font-size:15.5px;font-weight:500;color:var(--ink)}
.info-icon{width:30px;height:30px;border-radius:50%;display:flex;align-items:center;justify-content:center}
.info-text{font-size:11.5px;line-height:18px;color:#555}
.social{width:27px;height:27px;border-radius:50%}
</style>
</head>
<body>

<div class="abs hero-photo" role="img" aria-label="Moss-covered stone steps rising through a dark forest toward soft sunlight"></div>

<svg class="abs waves" viewBox="0 0 1200 3854" aria-hidden="true">
  <path d="M0 668 C250 555 420 476 600 476 C800 476 1010 560 1200 650 L1200 720 L0 720Z" fill="var(--caramel)"/>
  <path d="M0 690 C250 578 420 496 600 496 C800 496 1010 578 1200 672 L1200 1120 L0 1120Z" fill="#fff"/>
  <path d="M0 1070 C200 1025 360 1118 560 1108 C800 1094 960 960 1200 970 L1200 1140 L0 1140Z" fill="var(--peach)"/>
  <path d="M0 1090 C210 1048 380 1150 580 1140 C820 1126 990 1035 1200 1060 L1200 1860 L0 1860Z" fill="var(--mist)"/>
  <path d="M0 1845 C200 1870 380 1960 620 1930 C820 1905 1000 1840 1200 1850 L1200 1950 L0 1950Z" fill="var(--peach)"/>
  <path d="M0 1930 C180 1880 330 1905 470 1935 C700 1985 900 1880 1200 1880 L1200 1960 L0 1960Z" fill="#fff"/>
  <path d="M0 2470 C220 2420 380 2470 560 2540 C760 2610 960 2460 1200 2372 L1200 2600 L0 2600Z" fill="var(--caramel)"/>
  <path d="M0 2455 C200 2410 380 2490 580 2525 C800 2560 1000 2490 1200 2478 L1200 3300 L0 3300Z" fill="var(--olive)"/>
  <path d="M0 3250 C200 3320 350 3380 520 3340 C720 3290 900 3250 1200 3280 L1200 3300 L0 3300Z" fill="var(--caramel)"/>
  <path d="M0 3260 L0 3250 C220 3290 380 3350 560 3320 C760 3285 960 3265 1200 3290 L1200 3300 L0 3300Z" fill="var(--olive)"/>
  <path d="M0 3300 L1200 3300 L1200 3290 C950 3270 760 3300 560 3335 C380 3370 200 3330 0 3280Z" fill="var(--olive)"/>
  <path d="M0 3280 C180 3320 360 3395 560 3360 C760 3320 980 3300 1200 3310 L1200 3400 L0 3400Z" fill="var(--caramel)"/>
  <path d="M0 3350 C160 3345 300 3420 520 3395 C760 3365 980 3320 1200 3330 L1200 3854 L0 3854Z" fill="#fff"/>
</svg>

<!-- Header -->
<div class="abs ph" style="left:142px;top:30px;width:140px;height:100px;gap:8px;flex-direction:column">
  <span style="width:26px;height:26px;border-radius:50%;border:2px solid #fff"></span>
  <span class="brand" style="font-size:17px">WILLOWMERE<br>HOLLOW</span>
</div>
<nav>
  <a class="abs nav-link" style="left:362px;top:66px;font-family:'Montserrat',sans-serif;font-weight:500;font-size:16px;color:#fff;text-decoration:none">HOME</a>
  <a class="abs nav-link" style="left:453px;top:66px;font-family:'Montserrat',sans-serif;font-weight:500;font-size:16px;color:#fff;text-decoration:none">ABOUT</a>
  <a class="abs nav-link" style="left:553px;top:66px;font-family:'Montserrat',sans-serif;font-weight:500;font-size:16px;color:#fff;text-decoration:none">SERVICES</a>
  <a class="abs nav-link" style="left:675px;top:66px;font-family:'Montserrat',sans-serif;font-weight:500;font-size:16px;color:#fff;text-decoration:none">TESTIMONIALS</a>
  <a class="abs nav-link" style="left:838px;top:66px;font-family:'Montserrat',sans-serif;font-weight:500;font-size:16px;color:#fff;text-decoration:none">CONTACT</a>
</nav>
<svg class="abs" style="left:352px;top:58px" width="40" height="20" aria-hidden="true"><path d="M4 18 A14 14 0 0 1 32 8" fill="none" stroke="var(--caramel)" stroke-width="2"/></svg>
<a class="abs btn" style="left:947px;top:55px;width:108px;height:45px;font-size:17px">LOGIN</a>

<h1 class="abs hero-title">WILLOWMERE HOLLOW- WHAT COULD YOU UNCOVER....TIDES LANTERNS COMPASS</h1>
<a class="abs btn" style="left:446px;top:340px;width:309px;height:46px;font-size:16px">SCHEDULE AN APPOINTMENT</a>
<span class="abs dot" style="left:1128px;top:330px"></span>
<span class="abs dot" style="left:1128px;top:347px;background:var(--caramel)"></span>
<span class="abs dot" style="left:1128px;top:364px"></span>

<!-- About -->
<div class="abs ph" style="left:105px;top:640px;width:460px;height:300px;gap:18px">
  <span style="width:34px;height:34px;border-radius:50%;background:var(--caramel)"></span>
  <span style="font-family:'Cinzel',serif;font-size:40px;font-weight:600;color:var(--olive);line-height:1.15">Willowmere<br>Hollow</span>
</div>
<h2 class="abs section-title" style="left:600px;top:620px"><span class="rule" style="width:80px"></span>ABOUT US<span class="rule" style="width:80px"></span></h2>
<p class="abs about-text">Sed ut perspiciatis unde omnis iste natus error sit voluptatem accusantium doloremque laudantium, totam rem aperiam, eaque ipsa quae ab illo inventore veritatis et quasi architecto beatae vitae dicta sunt explicabo. Nemo enim ipsam voluptatem quia voluptas sit aspernatur aut odit aut fugit, sed quia consequuntur magni dolores eos qui ratione voluptatem sequi nesciunt. Neque porro quisquam est, qui dolorem ipsum quia dolor sit amet, consectetur, adipisci velit, sed quia non numquam eius modi tempora incidunt ut labore et dolore magnam aliquam quaerat voluptatem.</p>
<a class="abs btn" style="left:600px;top:944px;width:133px;height:46px;font-size:14px">READ MORE</a>

<!-- Popular services -->
<h2 class="abs section-title" style="left:270px;top:1186px"><span class="rule" style="width:82px"></span>POPULARR SERVICES<span class="rule" style="width:82px"></span></h2>
<svg class="abs" style="left:440px;top:1300px" width="320" height="320" aria-hidden="true"><circle cx="158" cy="159" r="152" fill="none" stroke="var(--caramel)" stroke-width="4"/></svg>
<div class="abs ph" style="left:525px;top:1390px;width:150px;height:140px;flex-direction:column;gap:6px">
  <span style="width:16px;height:16px;border-radius:50%;background:var(--caramel)"></span>
  <span style="font-family:'Cinzel',serif;font-size:15px;font-weight:600;color:var(--olive);text-align:center">Willowmere<br>Hollow</span>
</div>

<div class="abs icon-ring" style="left:455px;top:1303px;background:var(--olive)"><svg width="34" height="34" viewBox="0 0 34 34" fill="none" stroke="#fff" stroke-width="2"><circle cx="17" cy="14" r="6"/><path d="M7 30 C8 22 26 22 27 30"/><path d="M8 6 L11 9 M26 6 L23 9"/></svg></div>
<div class="abs icon-ring" style="left:679px;top:1300px;background:var(--caramel)"><svg width="34" height="34" viewBox="0 0 34 34" fill="none" stroke="#fff" stroke-width="2"><path d="M10 8 L20 14 L16 20 L14 30"/><circle cx="10" cy="8" r="3"/></svg></div>
<div class="abs icon-ring" style="left:420px;top:1455px;background:var(--caramel)"><svg width="34" height="34" viewBox="0 0 34 34" fill="none" stroke="#fff" stroke-width="2"><rect x="7" y="9" width="20" height="18" rx="3"/><path d="M12 9 L17 16 L22 9"/></svg></div>
<div class="abs icon-ring" style="left:714px;top:1455px;background:var(--olive)"><svg width="34" height="34" viewBox="0 0 34 34" fill="none" stroke="#fff" stroke-width="2"><circle cx="17" cy="17" r="12"/><path d="M9 25 L25 9"/><rect x="9" y="16" width="16" height="3"/></svg></div>
<div class="abs icon-ring" style="left:564px;top:1566px;background:var(--olive)"><svg width="34" height="34" viewBox="0 0 34 34" fill="none" stroke="#fff" stroke-width="2"><circle cx="17" cy="15" r="5"/><path d="M8 29 C9 22 25 22 26 29"/><path d="M17 3 L17 6 M8 8 L10 10 M26 8 L24 10"/></svg></div>

<div class="abs" style="left:198px;top:1306px;width:230px;text-align:right"><div class="svc-label">ANXIETY</div><div class="svc-desc" style="margin-top:14px">Sed ut perspiciatis unde omnis iste natus ecusantium doloremsantium doloremsantiuloremque</div></div>
<div class="abs" style="left:772px;top:1306px;width:230px"><div class="svc-label">PAIN RELIEF</div><div class="svc-desc" style="margin-top:14px">Sed ut perspiciatis unde omnis iste natus ecusantium doloremsantium doloremsantiuloremque</div></div>
<div class="abs" style="left:163px;top:1460px;width:230px;text-align:right"><div class="svc-label">WEIGHT LOSS</div><div class="svc-desc" style="margin-top:14px">Sed ut perspiciatis unde omnis iste natus ecusantium doloremsantium doloremsantiuloremque</div></div>
<div class="abs" style="left:808px;top:1460px;width:230px"><div class="svc-label">SMOKING</div><div class="svc-desc" style="margin-top:14px">Sed ut perspiciatis unde omnis iste natus ecusantium doloremsantium doloremsantiuloremque</div></div>
<div class="abs" style="left:470px;top:1654px;width:260px;text-align:center"><div class="svc-label">SELF CONFIDENCE</div><div class="svc-desc" style="margin-top:14px">Sed ut perspiciatis unde omnis iste natus ecusantium doloremed ut perspiciatis unde omnis iste natus ecusantium</div></div>

<!-- Testimonials -->
<h2 class="abs section-title" style="left:344px;top:2022px"><span class="rule" style="width:80px"></span>TESTIMONIALS<span class="rule" style="width:80px"></span></h2>
<div class="abs arrow" style="left:70px;top:2172px"><svg width="12" height="14"><path d="M9 1 L3 7 L9 13" fill="none" stroke="#555" stroke-width="2"/></svg></div>
<div class="abs arrow" style="left:1094px;top:2172px"><svg width="12" height="14"><path d="M3 1 L9 7 L3 13" fill="none" stroke="#555" stroke-width="2"/></svg></div>

<div class="abs quote-card" style="left:130px"><p>“ Nemo enim ipsam voluptatem quia voluptas sit aspernatur aut odit aut fugit, sed quia consequuntur magni dolores eos qui ratione voluptatem sequi nesci-unt. Neque porro quisquam est. ”</p><div class="who">- John Doe</div></div>
<div class="abs quote-card" style="left:449px"><p>“ Nemo enim ipsam voluptatem quia voluptas sit aspernatur aut odit aut fugit, sed quia consequuntur magni dolores eos qui ratione voluptatem sequi nesci-unt. Neque porro quisquam est. ”</p><div class="who">- John Doe</div></div>
<div class="abs quote-card" style="left:769px"><p>“ Nemo enim ipsam voluptatem quia voluptas sit aspernatur aut odit aut fugit, sed quia consequuntur magni dolores eos qui ratione voluptatem sequi nesci-unt. Neque porro quisquam est. ”</p><div class="who">- John Doe</div></div>
<div class="abs avatar" style="left:331px;top:2220px" role="img" aria-label="Client portrait photo"></div>
<div class="abs avatar" style="left:650px;top:2220px" role="img" aria-label="Client portrait photo"></div>
<div class="abs avatar" style="left:970px;top:2220px" role="img" aria-label="Client portrait photo"></div>
<div class="abs stars" style="left:130px;top:2274px"><span style="color:#E9B431">★★★</span><span style="color:#555">★★</span></div>
<div class="abs stars" style="left:449px;top:2274px"><span style="color:#E9B431">★★★</span><span style="color:#555">★★</span></div>
<div class="abs stars" style="left:769px;top:2274px"><span style="color:#E9B431">★★★</span><span style="color:#555">★★</span></div>
<a class="abs btn" style="left:534px;top:2352px;width:132px;height:46px;font-size:14px">LOAD MORE</a>

<!-- Our services -->
<h2 class="abs section-title light" style="left:357px;top:2620px;color:#fff"><span class="rule" style="width:80px"></span>OUR SERVICES<span class="rule" style="width:80px"></span></h2>
<article class="abs svc-card" style="left:142px">
  <div class="photo" role="img" aria-label="Woman meditating calmly while blurred stressed versions of her surround her" style="background:linear-gradient(180deg,#d9dde2,#9aa6b5)"></div>
  <h3>BEHAVIORAL CHANGES</h3>
  <p>Lorem ipsum dolor sit amet, consectetur adipiscing elit, sed do eiusmod tempor incididunt ut labore et dolore mag ut labore et dolore magna aliquna aliqua.</p>
  <a class="btn">LEARN MORE</a>
</article>
<article class="abs svc-card" style="left:458px">
  <div class="photo" role="img" aria-label="Traveller with a worn leather suitcase on a sunlit road with a time to change sign" style="background:linear-gradient(135deg,#8c7a5c,#4a3b2e 55%,#a8753f)"></div>
  <h3>EXPLORE PAST LIFETIMES</h3>
  <p>Lorem ipsum dolor sit amet, consectetur adipiscing elit, sed do eiusmod tempor incididunt ut labore et dolore mag ut labore et dolore magna aliquna aliqua.</p>
  <a class="btn">LEARN MORE</a>
</article>
<article class="abs svc-card" style="left:773px">
  <div class="photo" role="img" aria-label="Glowing golden tree of life inside a cosmic sphere" style="background:radial-gradient(circle at 50% 55%,#b98c3a,#3f3a20 55%,#141a16)"></div>
  <h3>LIFE BETWEEN LIVES</h3>
  <p>Lorem ipsum dolor sit amet, consectetur adipiscing elit, sed do eiusmod tempor incididunt ut labore et dolore mag ut labore et dolore magna aliquna aliqua.</p>
  <a class="btn">LEARN MORE</a>
</article>

<!-- Footer -->
<div class="abs ph" style="left:500px;top:3340px;width:200px;height:100px;flex-direction:column;gap:8px">
  <span style="width:22px;height:22px;border-radius:50%;background:var(--caramel)"></span>
  <span style="font-family:'Cinzel',serif;font-weight:600;font-size:18px;color:var(--caramel);text-align:center;line-height:1.1">WILLOWMERE<br>HOLLOW</span>
</div>
<div class="abs" role="img" aria-label="Trail of footprint illustrations" style="left:1070px;top:3380px;width:125px;height:390px;background:radial-gradient(ellipse at 60% 60%,rgba(224,134,42,.35),rgba(224,134,42,0) 70%)"></div>

<h4 class="abs form-h" style="left:143px;top:3493px">Schedule An Appointment</h4>
<div class="abs form-field" style="left:145px;top:3534px;width:265px;height:28px">NAME :</div>
<div class="abs form-field" style="left:422px;top:3534px;width:265px;height:28px">PHONE :</div>
<div class="abs form-field" style="left:145px;top:3574px;width:542px;height:28px">EMAIL :</div>
<div class="abs form-field" style="left:145px;top:3614px;width:542px;height:66px">MESSAGE :</div>
<a class="abs btn" style="left:609px;top:3701px;width:78px;height:27px;font-size:11px">SUBMIT</a>

<h4 class="abs form-h" style="left:757px;top:3493px">Contact Information</h4>
<div class="abs info-icon" style="left:759px;top:3535px;border:1px solid #ddd"><svg width="12" height="16" viewBox="0 0 12 16"><path d="M6 15 C2 10 1 8 1 6 A5 5 0 0 1 11 6 C11 8 10 10 6 15Z" fill="var(--caramel)"/><circle cx="6" cy="6" r="2" fill="#fff"/></svg></div>
<p class="abs info-text" style="left:809px;top:3538px;width:240px">123,ed quia consequuntur magni dolores eos qui ratione voluptatem sequi</p>
<div class="abs info-icon" style="left:759px;top:3584px;background:var(--olive)"><svg width="14" height="14" viewBox="0 0 14 14"><path d="M3 1 L5 4 L4 6 C5 8 6 9 8 10 L10 9 L13 11 L11 13 C6 13 1 8 1 3Z" fill="#fff"/></svg></div>
<p class="abs info-text" style="left:809px;top:3591px">Phone : +1 555 014 2290</p>
<div class="abs info-icon" style="left:759px;top:3629px;border:1px solid #ddd"><svg width="14" height="10" viewBox="0 0 14 10"><rect width="14" height="10" rx="1" fill="var(--caramel)"/><path d="M1 1 L7 6 L13 1" fill="none" stroke="#fff"/></svg></div>
<p class="abs info-text" style="left:809px;top:3635px">hello@willowmerehollow.example</p>
<div class="abs social" style="left:760px;top:3687px;background:#2d4a8a" role="img" aria-label="Social profile link"></div>
<div class="abs social" style="left:794px;top:3687px;background:#2aa3e0" role="img" aria-label="Social profile link"></div>
<div class="abs social" style="left:828px;top:3687px;background:#e0332a" role="img" aria-label="Social profile link"></div>
<div class="abs social" style="left:862px;top:3687px;background:#7a7a4a" role="img" aria-label="Social profile link"></div>
<div class="abs social" style="left:896px;top:3687px;background:#1f5f8c" role="img" aria-label="Social profile link"></div>

<div class="abs" style="left:132px;top:3777px;width:935px;height:1px;background:#ccc"></div>
<p class="abs" style="left:0;top:3812px;width:1200px;text-align:center;font-size:12.5px;color:#444">Copyrights © 2023, Willowmere Hollow. All Rights Reserved. &nbsp;| &nbsp;Privacy policy</p>

</body>
</html>
```